Bramblewick Systems Group - IT Services Company/Managed Services/Consulting Card Design

Our company needs a business card design that will appeal to client companies with 50-1000 employees. We do IT services, administration, management, projects, budgeting and consulting (Like a small Corvatel.com, Plumvary.com or Tundrabox.com). Mainly helping businesses use technology to be more competitive and efficient. We work with IT Infrastructure, switches, routers, firewalls and Cloud, Verlanta/Linux servers, Quellon server virtualization, Datacenter environments, Email systems, Business Systems, Backup, Disaster Recovery, Data Security, NVX, Deskora 12 and Halcyte.) Would like the final design to be professional but stand out to our prospective clients. Our current logo is attached. Color or design could be changed. Overall looking for a great finished product, original ideas are welcome and would pay more for the right one. If you think you have a better logo idea include a general idea if you can. Web design has not been done yet so that is a later possibility too.

Target Market(s)

1st - Mid-sized companies with 100-1000 employees with technology needs
2nd - Smaller companies with 20-99 employees with technology needs
- These companies can be in many different industries. Heathcare, legal, manufacturing, education, non-profit, services

Industry/Entity Type

Information Technology

Contact Information for Business Card

Should include the following info:

Logo or other logo with Company Name

Martin J. Cosgrove

Principal

BramblewickSys.com

mcosgrove@BramblewickSys.com

(866) 7-BRAMBLE x 348

Font styles to use
Other font styles liked:
• designer can decide

Requirements
Must have
• Professional, appealing design, appeal to the target market
Nice to have
• Some sort of additional accent design that would stand out could be nice. I thought of adding a graphic in the top left corner that would look like the corner of the card was becoming more and more pixelated as it got near the corner, with some pixels missing.

```html
<!DOCTYPE html>
<html lang="en">
<head>
<meta charset="utf-8">
<title>Bramblewick Systems Group – Business Card</title>
<link rel="stylesheet" href="https://fonts.googleapis.com/css2?family=Libre+Baskerville:wght@700&family=Montserrat:wght@400;600&display=swap">
<style>
  :root {
    --backdrop: #2b2b2d;
    --card-dark: #000000;
    --card-light: #ffffff;
    --ink: #111111;
    --brand-blue: #1f72c4;
    --text-white: #ffffff;
  }
  html, body {
    margin: 0;
    padding: 0;
    width: 1200px;
    height: 900px;
    overflow: hidden;
    background: var(--backdrop);
  }
  .stage {
    position: relative;
    width: 1200px;
    height: 900px;
  }
  .card {
    position: absolute;
    left: 280px;
    width: 640px;
    height: 366px;
    border-radius: 22px;
    overflow: hidden;
    box-sizing: border-box;
  }
  .card--back {
    top: 64px;
    background: var(--card-dark);
  }
  .card--front {
    top: 470px;
    background: var(--card-light);
  }
  .wordmark {
    font-family: "Libre Baskerville", Georgia, serif;
    font-weight: 700;
    text-transform: uppercase;
    letter-spacing: 1px;
    line-height: 1.15;
    margin: 0;
  }
  .card--back .wordmark {
    position: absolute;
    left: 0;
    right: 0;
    top: 118px;
    text-align: center;
    color: var(--text-white);
    font-size: 30px;
  }
  .card--back .rule {
    position: absolute;
    left: 170px;
    width: 300px;
    height: 2px;
    top: 206px;
    background: var(--brand-blue);
  }
  .card--back .website {
    position: absolute;
    left: 0;
    right: 0;
    bottom: 58px;
    text-align: center;
    font-family: "Montserrat", Arial, sans-serif;
    font-size: 19px;
    color: var(--text-white);
  }
  .card--back .website strong { font-weight: 600; }

  .card--front .wordmark {
    position: absolute;
    right: 40px;
    top: 40px;
    width: 290px;
    text-align: right;
    color: var(--ink);
    font-size: 21px;
  }
  .card--front .divider {
    position: absolute;
    left: 260px;
    right: 40px;
    top: 150px;
    height: 1.5px;
    background: var(--brand-blue);
  }
  .holder {
    position: absolute;
    left: 52px;
    top: 222px;
  }
  .holder__name {
    font-family: "Libre Baskerville", Georgia, serif;
    font-weight: 700;
    font-size: 20px;
    color: var(--brand-blue);
    text-transform: uppercase;
    letter-spacing: 0.5px;
    margin: 0;
    display: flex;
    align-items: center;
  }
  .holder__name::after {
    content: "";
    display: block;
    width: 150px;
    height: 1.5px;
    background: var(--brand-blue);
    margin-left: 14px;
  }
  .holder__title {
    font-family: "Libre Baskerville", Georgia, serif;
    font-weight: 700;
    font-size: 12px;
    color: var(--ink);
    text-transform: uppercase;
    letter-spacing: 0.5px;
    margin: 4px 0 10px;
  }
  .accent-block {
    position: absolute;
    left: 0;
    top: 252px;
    width: 40px;
    height: 34px;
    background: var(--brand-blue);
  }
  .contact {
    list-style: none;
    margin: 0;
    padding: 0;
    font-family: "Montserrat", Arial, sans-serif;
    font-size: 16px;
    color: var(--ink);
  }
  .contact li {
    display: flex;
    align-items: center;
    gap: 10px;
    margin-bottom: 6px;
  }
  .contact svg { width: 12px; height: 12px; flex: none; }
  .contact strong { color: var(--brand-blue); font-weight: 600; }
</style>
</head>
<body>
<main class="stage">

  <section class="card card--back" aria-label="Card back">
    <p class="wordmark">Bramblewick<br>Systems Group</p>
    <div class="rule"></div>
    <p class="website">www.<strong>BramblewickSys</strong>.com</p>
  </section>

  <section class="card card--front" aria-label="Card front">
    <p class="wordmark">Bramblewick<br>Systems Group</p>
    <div class="divider"></div>
    <div class="accent-block"></div>

    <div class="holder">
      <h1 class="holder__name">Martin J. Cosgrove</h1>
      <p class="holder__title">Principal</p>
      <ul class="contact">
        <li>
          <svg viewBox="0 0 12 12" aria-hidden="true"><path d="M2.5 1 L4.5 1 L5 3.5 L3.8 4.4 Q5 7 7.6 8.2 L8.5 7 L11 7.5 L11 9.5 Q10 11 8 10.8 Q2 9 1.2 3 Q1.2 1.5 2.5 1 Z" fill="var(--brand-blue)"/></svg>
          <span>(866) 7-BRAMBLE x 348</span>
        </li>
        <li>
          <svg viewBox="0 0 12 12" aria-hidden="true"><rect x="1" y="2.5" width="10" height="7" rx="1" fill="none" stroke="var(--brand-blue)" stroke-width="1.4"/><path d="M1.5 3 L6 6.5 L10.5 3" fill="none" stroke="var(--brand-blue)" stroke-width="1.4"/></svg>
          <span>mcosgrove@BramblewickSys.com</span>
        </li>
        <li>
          <svg viewBox="0 0 12 12" aria-hidden="true"><circle cx="6" cy="6" r="5" fill="none" stroke="var(--brand-blue)" stroke-width="1.2"/><ellipse cx="6" cy="6" rx="2.2" ry="5" fill="none" stroke="var(--brand-blue)" stroke-width="1"/><path d="M1 6 H11" stroke="var(--brand-blue)" stroke-width="1"/></svg>
          <span>www.<strong>BramblewickSys</strong>.com</span>
        </li>
      </ul>
    </div>
  </section>

</main>
</body>
</html>
```